Powerpoint and Word template required

We need PowerPoint and Word templates for all of our company branded materials and stationary. We have recently rebranded our website and would like something that is reflective of our new corporate branding. A sample of some of the documents we have created recently are attached and our website is below

http://lorventamedical.com.au/

The word template will be used for all letters we send to clients and customers and we think we want the logo and ISO 9001 cert to only appear on the first page.

The powerpoint template has to be flexible as we use this for both marketing and training purposes. I have attached a couple of samples of the types of documents we create and note that these are very basic / crude and we would be looking for something that is a significant improvement on these

In the powerpoint template it would be good to have lots of standard layouts within the template, e.g. different 'standard layouts for multiple elements on a page including pictures and text etc.
Updates

Project Deadline Extended
Reason: Still looking for a professional yet modern template and important to us that we can see more tan just a title slide and the layout of the other slide master slides is very important to us. Many thanks, Doug

Industry/Entity Type

Healthcare

Font styles to use
Sans Serif

Colors
33a6d7

Requirements
Must have
• Templates must be versatile for use; powerpoint template must be able to be used for training materials and weel as marketing / pitch books.
• Word template must be able to be used as a basis for our corporate letter head through to RFP response type documents as well as Reference / Operating manual type of documents
• In terms of the design it must be consistent with our new corporate image which is best represented by our new website design; www.lorventamedical.com

```html
<!DOCTYPE html>
<html lang="en">
<head>
<meta charset="utf-8">
<title>Lorventa Slide Master Layouts</title>
<link href="https://fonts.googleapis.com/css2?family=Montserrat:wght@400;600;700&display=swap" rel="stylesheet">
<style>
:root{
  --brand:#33a6d7;
  --brand-deep:#1c8cc2;
  --brand-light:#4cc6e6;
  --ink-blue:#2a6cb3;
  --head-pale:#dff2fb;
  --grey-1:#dfe4e8;
  --grey-2:#a9b4ba;
  --grey-3:#8a9aa2;
  --text:#444;
  --frame:#111;
  --paper:#fff;
  --wm:rgba(51,166,215,.2);
}
*{box-sizing:border-box;margin:0;padding:0}
html,body{width:971px;height:1200px;overflow:hidden;background:var(--paper)}
body{position:relative;font-family:"Montserrat",Arial,sans-serif;color:var(--text)}
.slide{position:absolute;width:433px;height:244px;border:2px solid var(--frame);background:var(--paper);overflow:hidden}
.col-l{left:34px}.col-r{left:506px}
.row-1{top:20px}.row-2{top:310px}.row-3{top:610px}.row-4{top:909px}
.band{position:absolute;left:0;width:100%}
.band-grey{background:linear-gradient(180deg,var(--grey-1),var(--grey-2) 60%,var(--grey-3))}
.band-blue{background:linear-gradient(180deg,var(--brand-light),var(--brand) 50%,var(--brand-deep))}
.band-head{background:linear-gradient(180deg,var(--brand-light),var(--brand) 60%,var(--brand-deep))}
.heading{position:absolute;font-weight:700;letter-spacing:2.5px;text-transform:uppercase;font-size:21px}
.heading.pale{color:var(--head-pale)}
.heading.ink{color:var(--ink-blue)}
.wordmark{position:absolute;display:flex;align-items:center;gap:9px;color:var(--ink-blue);font-weight:700}
.wordmark .mark{background:currentColor;border-radius:3px}
.wordmark.faint{color:var(--wm)}
.body-lines{position:absolute;font-size:10.2px;line-height:17.2px;letter-spacing:.4px;color:#555}
.small{position:absolute;font-size:7.5px;line-height:12.5px;color:#333}
.small p+p{margin-top:12.5px}
.list{position:absolute;font-size:6.2px;color:#223;list-style:none}
.list li{height:27.5px}
.divider{position:absolute;left:214px;top:60px;width:5px;height:184px;background:rgba(255,255,255,.6)}
.placeholder{position:absolute;left:16px;top:62px;width:119px;height:120px;border:2px solid var(--frame);background:transparent}
.placeholder span{position:absolute;top:20px;left:0;width:100%;text-align:center;font-weight:700;font-size:11.5px;letter-spacing:1px;color:var(--frame)}
.placeholder svg{position:absolute;inset:0}
.content-label{position:absolute;left:14px;top:104px;font-weight:700;font-size:21px;letter-spacing:1.5px;color:var(--frame)}
</style>
</head>
<body>

<section class="slide col-l row-1" aria-label="Title slide">
  <div class="band band-grey" style="top:0;height:76px"></div>
  <div class="band band-blue" style="top:168px;height:76px"></div>
  <div class="wordmark" style="left:118px;top:98px;font-size:34px">
    <span class="mark" style="width:40px;height:40px"></span>Lorventa
  </div>
</section>

<section class="slide col-r row-1" aria-label="Title and content">
  <div class="band band-head" style="top:0;height:54px"></div>
  <h2 class="heading pale" style="left:38px;top:15px">Title</h2>
  <div class="body-lines" style="left:38px;top:72px">
    Lorem ipsum dolor sit amet, consectetur adipiscing elit.<br>
    Vivamus sit amet urna non massa sagittis suscipit quis sed libero.<br>
    Nullam ultricies nisi at risus pretium laoreet sit amet sit amet eros.<br>
    Nam feugiat nisi id tortor consectetur, a bibendum dolor pharetra.<br>
    Cras placerat nisi et luctus lacinia.<br>
    In viverra nibh sed neque fringilla, vitae gravida diam hendrerit.<br>
    Vivamus sollicitudin mi eget dui dignissim dignissim.<br>
    Fusce dignissim massa a odio eleifend placerat.
  </div>
</section>

<section class="slide col-l row-2" aria-label="Section header">
  <div class="wordmark faint" style="left:46px;top:48px;font-size:62px">
    <span class="mark" style="width:72px;height:72px"></span>Lorventa
  </div>
  <div class="band band-head" style="top:160px;height:54px"></div>
  <h2 class="heading pale" style="left:40px;top:176px">Section Header</h2>
</section>

<section class="slide col-r row-2" aria-label="Two contents">
  <div class="band band-head" style="top:0;height:54px"></div>
  <h2 class="heading pale" style="left:19px;top:15px">Two Contents</h2>
  <div class="small" style="left:22px;top:66px;width:180px">
    <p>Lorem ipsum dolor sit amet, consectetuer adipiscing elit. Donec odio. Quisque volutpat mattis eros. Nullam malesuada erat ut turpis. Suspendisse urna nibh, viverra non, semper suscipit, posuere a, pede.</p>
    <p>Donec nec justo eget felis facilisis fermentum. Aliquam porttitor mauris sit amet orci. Aenean dignissim pellentesque felis.</p>
    <p>Morbi in sem quis dui placerat ornare. Pellen-tesque odio nisi, euismod in, pharetra a, ultricies in, diam. Sed arcu. Cras consequat.</p>
  </div>
  <div class="small" style="left:230px;top:66px;width:180px">
    <p>Lorem ipsum dolor sit amet, consectetuer adipiscing elit. Donec odio. Quisque volutpat mattis eros. Nullam malesuada erat ut turpis. Suspendisse urna nibh, viverra non, semper suscipit, posuere a, pede.</p>
    <p>Donec nec justo eget felis facilisis fermentum. Aliquam porttitor mauris sit amet orci. Aenean dignissim pellentesque felis.</p>
    <p>Morbi in sem quis dui placerat ornare. Pellen-tesque odio nisi, euismod in, pharetra a, ultricies in, diam. Sed arcu. Cras consequat.</p>
  </div>
</section>

<section class="slide col-l row-3" aria-label="Comparison" style="background:linear-gradient(180deg,var(--grey-2) 20%,#b8dbe6 45%,var(--brand-light) 70%,var(--brand-deep))">
  <div class="band band-grey" style="top:0;height:20px"></div>
  <div class="band" style="top:20px;height:40px;background:var(--paper)"></div>
  <h2 class="heading ink" style="left:0;width:100%;text-align:center;top:26px">Comparison</h2>
  <div class="divider"></div>
  <ol class="list" style="left:18px;top:80px">
    <li>1. Lorem ipsum dolor sit amet, consectetuer adipiscing elit.</li>
    <li>2. Aliquam tincidunt mauris eu risus.</li>
    <li>3. Vestibulum auctor dapibus neque.</li>
    <li>4. Nunc dignissim risus id metus.</li>
    <li>5. Cras ornare tristique elit.</li>
  </ol>
  <ol class="list" style="left:240px;top:80px">
    <li>1. Lorem ipsum dolor sit amet, consectetuer adipiscing elit.</li>
    <li>2. Aliquam tincidunt mauris eu risus.</li>
    <li>3. Vestibulum auctor dapibus neque.</li>
    <li>4. Nunc dignissim risus id metus.</li>
    <li>5. Cras ornare tristique elit.</li>
  </ol>
</section>

<section class="slide col-r row-3" aria-label="Blank" style="background:linear-gradient(180deg,var(--grey-1),var(--grey-2) 25%,#a8dbea 50%,var(--brand-light) 70%,var(--brand-deep))">
  <h2 class="heading ink" style="left:0;width:100%;text-align:center;top:105px">Blank</h2>
</section>

<section class="slide col-l row-4" aria-label="Picture with text">
  <div class="band band-grey" style="top:0;height:38px"></div>
  <div class="band band-blue" style="top:204px;height:40px"></div>
  <div class="wordmark faint" style="left:46px;top:82px;font-size:62px">
    <span class="mark" style="width:72px;height:72px"></span>Lorventa
  </div>
  <div class="placeholder" role="img" aria-label="Image placeholder">
    <svg width="115" height="116" viewBox="0 0 115 116"><line x1="0" y1="0" x2="115" y2="116" stroke="#111" stroke-width="1.5"/><line x1="115" y1="0" x2="0" y2="116" stroke="#111" stroke-width="1.5"/></svg>
    <span>IMAGE</span>
  </div>
  <div class="small" style="left:202px;top:70px;width:180px">
    <p>Lorem ipsum dolor sit amet, consectetuer adipiscing elit. Donec odio. Quisque volutpat mattis eros. Nullam malesuada erat ut turpis. Suspendisse urna nibh, viverra non, semper suscipit, posuere a, pede.</p>
    <p>Donec nec justo eget felis facilisis fermentum. Aliquam porttitor mauris sit amet orci. Aenean dignissim pellentesque felis.</p>
  </div>
</section>

<section class="slide col-r row-4" aria-label="Content with text">
  <div class="band band-grey" style="top:0;height:38px"></div>
  <div class="band band-blue" style="top:204px;height:40px"></div>
  <div class="wordmark faint" style="left:40px;top:82px;font-size:62px">
    <span class="mark" style="width:72px;height:72px"></span>Lorventa
  </div>
  <div class="content-label">CONTENT</div>
  <div class="small" style="left:200px;top:70px;width:180px">
    <p>Lorem ipsum dolor sit amet, consectetuer adipiscing elit. Donec odio. Quisque volutpat mattis eros. Nullam malesuada erat ut turpis. Suspendisse urna nibh, viverra non, semper suscipit, posuere a, pede.</p>
    <p>Donec nec justo eget felis facilisis fermentum. Aliquam porttitor mauris sit amet orci. Aenean dignissim pellentesque felis.</p>
  </div>
</section>

</body>
</html>
```